I need a business card design for a new company that will be doing consulting work around issues of cultural competency, and diversity and inclusion. I would like the design to be crisp and clear with bold but conservative colors and incorporate shades of blue

Target Market(s)

Small businesses, schools, non-profits

Industry/Entity Type

Consulting

Font styles to use
Serif
Sans Serif

Colors
0c5ba6
6b449b
3276b5
0292cd

Requirements
Must have
• A Morrow Venture (name of company)
• Lemlem Tavish
• CEO
• lemlem@amorrowventure.com
• (215)483-2756

```html
<!DOCTYPE html>
<html lang="en">
<head>
<meta charset="UTF-8">
<title>A Morrow Venture — Business Card</title>
<link rel="stylesheet" href="https://fonts.googleapis.com/css2?family=Cinzel:wght@500;600&family=Arimo:wght@400&display=swap">
<style>
  :root {
    --page-bg: #eef1f5;
    --card-blue: #0c5ba6;
    --brand-blue: #3276b5;
    --card-white: #ffffff;
    --text-on-blue: #ffffff;
  }
  html, body {
    margin: 0;
    padding: 0;
    width: 1200px;
    height: 900px;
    overflow: hidden;
    background: var(--page-bg);
  }
  .canvas {
    position: relative;
    width: 1200px;
    height: 900px;
  }
  .business-card {
    position: absolute;
    left: 150px;
    top: 172px;
    width: 900px;
    height: 556px;
    filter: drop-shadow(0 10px 24px rgba(12, 40, 80, 0.18));
  }
  .card-shape {
    position: absolute;
    inset: 0;
  }
  .company-name {
    position: absolute;
    left: 0;
    top: 0;
    width: 500px;
    height: 556px;
    display: flex;
    flex-direction: column;
    align-items: center;
    justify-content: center;
    margin: 0;
    font-family: "Cinzel", Georgia, serif;
    font-weight: 600;
    font-size: 50px;
    line-height: 1.15;
    letter-spacing: 1px;
    color: var(--brand-blue);
    text-align: center;
  }
  .holder {
    position: absolute;
    right: 55px;
    top: 56px;
    text-align: right;
    color: var(--text-on-blue);
  }
  .holder-name {
    margin: 0;
    font-family: "Cinzel", Georgia, serif;
    font-weight: 500;
    font-size: 31px;
    letter-spacing: 1.5px;
    line-height: 1.1;
  }
  .holder-title {
    margin: 6px 0 0;
    font-family: "Arimo", Arial, sans-serif;
    font-size: 24px;
    line-height: 1.1;
  }
  .contact-list {
    position: absolute;
    right: 55px;
    top: 437px;
    margin: 0;
    padding: 0;
    list-style: none;
    font-family: "Arimo", Arial, sans-serif;
    font-size: 23px;
    color: var(--text-on-blue);
    text-align: right;
  }
  .contact-item {
    display: flex;
    align-items: center;
    justify-content: flex-end;
    gap: 10px;
    height: 33px;
  }
  .contact-icon {
    width: 20px;
    height: 20px;
    flex: none;
  }
</style>
</head>
<body>
<div class="canvas">
  <div class="business-card">
    <svg class="card-shape" width="900" height="556" viewBox="0 0 900 556" aria-hidden="true">
      <circle cx="278" cy="278" r="278" fill="var(--card-blue)"/>
      <rect x="278" y="0" width="622" height="556" fill="var(--card-blue)"/>
      <rect x="278" y="178" width="622" height="204" fill="var(--card-white)"/>
      <circle cx="278" cy="278" r="266" fill="var(--card-white)"/>
    </svg>

    <h1 class="company-name"><span>A Morrow</span><span>Venture</span></h1>

    <div class="holder">
      <p class="holder-name">Lemlem Tavish</p>
      <p class="holder-title">CEO</p>
    </div>

    <ul class="contact-list">
      <li class="contact-item">
        <span>(215)483-2756</span>
        <svg class="contact-icon" viewBox="0 0 20 20" aria-label="Phone">
          <path d="M2 7c0-3 3.5-4 8-4s8 1 8 4v1.5h-4V7c-1-0.8-7-0.8-8 0v1.5H2z" fill="currentColor"/>
          <path d="M5 10h10l2 7H3z" fill="currentColor"/>
          <circle cx="10" cy="13.5" r="2" fill="var(--card-blue)"/>
        </svg>
      </li>
      <li class="contact-item">
        <span>lemlem@amorrowventure.com</span>
        <svg class="contact-icon" viewBox="0 0 20 20" aria-label="Email">
          <rect x="2" y="4.5" width="16" height="11" fill="currentColor"/>
          <path d="M2.5 5l7.5 6 7.5-6" fill="none" stroke="var(--card-blue)" stroke-width="1.4"/>
        </svg>
      </li>
    </ul>
  </div>
</div>
</body>
</html>
```